roomhavenly.net banner ads

Hi All,

I'm looking for a set of banner ads designing for a Quorvix Promoads campaign for roomhavenly.net.

The website serves the UK and is a portal for people who cannot afford to buy or rent a place of their own, to find a room to let in someone else's house.

Conversely, home owners can pay to advertise a listing of their spare room. Have a look at the site, and you'll get the idea. Please bear in mind that it's a work in progress and is currently being developed and polished.

The banners do not have to be animated (no Flash please) but should cover all the standard sizes used by Quorvix Promoads.

Please take design guidance and inspiration from the web site itself. I'm looking for something eye-catching and creative.

Many thanks,
Leon

Target Market(s)

1. People who can't afford to buy or rent a property

Industry/Entity Type

House

Requirements
Must have
• The logo should be prominent in the ads

```html
<!DOCTYPE html>
<html lang="en">
<head>
<meta charset="utf-8">
<title>roomhavenly.net banner set</title>
<link rel="stylesheet" href="https://fonts.googleapis.com/css2?family=Oswald:wght@500&family=Arimo:wght@400;700&display=swap">
<style>
  :root {
    --bg-top: #e4e4e4;
    --bg-bottom: #ffffff;
    --orange-light: #ff7a12;
    --orange-dark: #f25a00;
    --photo-a: #b8ab8e;
    --photo-b: #6e5640;
    --arc-grey: #c9c9c9;
    --white: #ffffff;
    --brand-blue: #1e5f9a;
    --button-top: #5aa6e6;
    --button-bottom: #1c62a8;
    --button-edge: #e9eef3;
  }
  * { box-sizing: border-box; margin: 0; padding: 0; }
  html, body { width: 1200px; height: 871px; overflow: hidden; }
  body {
    background: linear-gradient(var(--bg-top), var(--bg-bottom) 75%);
    position: relative;
    font-family: "Arimo", Arial, sans-serif;
  }
  .banner {
    position: absolute;
    overflow: hidden;
    background: linear-gradient(var(--orange-light), var(--orange-dark));
    color: var(--white);
  }
  .banner svg.backdrop { position: absolute; left: 0; top: 0; }
  .headline {
    position: absolute;
    font-family: "Oswald", "Arial Narrow", sans-serif;
    font-weight: 500;
    letter-spacing: -0.3px;
    text-shadow: 0 1px 2px rgba(0,0,0,.25);
    white-space: nowrap;
  }
  .tagline { position: absolute; white-space: nowrap; }
  .brand-name {
    position: absolute;
    font-weight: 700;
    color: var(--brand-blue);
    white-space: nowrap;
  }
  .brand-name.on-orange { color: var(--white); }
  .cta {
    position: absolute;
    display: flex;
    align-items: center;
    justify-content: center;
    background: linear-gradient(var(--button-top), var(--button-bottom));
    border: 3px solid var(--button-edge);
    box-shadow: 0 2px 3px rgba(0,0,0,.35);
    color: var(--white);
    font-size: 21px;
  }

  /* skyscraper 199 x 745 */
  .skyscraper { left: 42px; top: 78px; width: 199px; height: 745px; }
  .skyscraper .headline { left: 0; width: 199px; top: 312px; text-align: center; font-size: 40px; line-height: 50px; }
  .skyscraper .tagline { left: 0; width: 199px; top: 433px; text-align: center; font-size: 26px; line-height: 33px; }
  .skyscraper .brand-name { left: 0; width: 199px; top: 645px; text-align: center; font-size: 20px; }
  .skyscraper .cta { left: 17px; top: 683px; width: 164px; height: 40px; }

  /* medium rectangle 372 x 310 */
  .rectangle { top: 359px; width: 372px; height: 310px; }
  .rectangle.first { left: 267px; }
  .rectangle.second { left: 669px; }
  .rectangle .brand-name { left: 0; width: 372px; top: 12px; text-align: center; font-size: 22px; }
  .rectangle .headline { left: 0; width: 372px; top: 170px; text-align: center; font-size: 36px; line-height: 48px; }
  .rectangle .tagline { left: 0; width: 372px; top: 225px; text-align: center; font-size: 20px; }
  .rectangle .cta { left: 104px; top: 258px; width: 164px; height: 40px; }

  /* leaderboard 903 x 112 */
  .leaderboard { left: 267px; top: 711px; width: 903px; height: 112px; }
  .leaderboard .headline { left: 292px; top: 8px; font-size: 38px; line-height: 50px; }
  .leaderboard .tagline { left: 292px; top: 67px; font-size: 21px; }
  .leaderboard .brand-name { left: 645px; top: 14px; font-size: 24px; color: var(--white); }
  .leaderboard .cta { left: 697px; top: 56px; width: 163px; height: 40px; }
</style>
</head>
<body>
  <svg width="0" height="0" aria-hidden="true">
    <defs>
      <linearGradient id="photo-tone" x1="0" y1="0" x2="0.6" y2="1">
        <stop offset="0" stop-color="#d8d0bb"/>
        <stop offset="0.55" stop-color="#a7977b"/>
        <stop offset="1" stop-color="#5e4632"/>
      </linearGradient>
    </defs>
  </svg>

  <section class="banner skyscraper">
    <svg class="backdrop" width="199" height="745" viewBox="0 0 199 745">
      <path d="M0 244 Q105 305 199 250" fill="none" stroke="var(--arc-grey)" stroke-width="10"/>
      <path d="M0 0H199V240Q105 295 0 232Z" fill="url(#photo-tone)" role="img" aria-label="Photo of a bright home kitchen with washing machine and wooden floor"/>
    </svg>
    <div class="headline">Looking for<br>a lodger?</div>
    <div class="tagline">great way<br>to find<br>a suitable<br>lodger</div>
    <div class="brand-name on-orange">roomhavenly.net</div>
    <div class="cta">Click Here!</div>
  </section>

  <section class="banner rectangle first">
    <svg class="backdrop" width="372" height="310" viewBox="0 0 372 310">
      <path d="M0 82 Q170 190 372 76" fill="none" stroke="var(--arc-grey)" stroke-width="10"/>
      <path d="M0 0H372V64Q170 180 0 72Z" fill="url(#photo-tone)" role="img" aria-label="Photo of a home kitchen with washing machine and worktops"/>
    </svg>
    <div class="brand-name">roomhavenly.net</div>
    <div class="headline">Looking for a lodger?</div>
    <div class="tagline">great way to find a suitable lodger</div>
    <div class="cta">Click Here!</div>
  </section>

  <section class="banner rectangle second">
    <svg class="backdrop" width="372" height="310" viewBox="0 0 372 310">
      <path d="M0 82 Q170 190 372 76" fill="none" stroke="var(--arc-grey)" stroke-width="10"/>
      <path d="M0 0H372V64Q170 180 0 72Z" fill="url(#photo-tone)" role="img" aria-label="Photo of a home kitchen with washing machine and worktops"/>
    </svg>
    <div class="brand-name">roomhavenly.net</div>
    <div class="headline">Looking for a lodger?</div>
    <div class="tagline">great way to find a suitable lodger</div>
    <div class="cta">Click Here!</div>
  </section>

  <section class="banner leaderboard">
    <svg class="backdrop" width="903" height="112" viewBox="0 0 903 112">
      <path d="M258 0 Q292 56 262 112" fill="none" stroke="var(--arc-grey)" stroke-width="10"/>
      <path d="M0 0H252Q284 56 256 112H0Z" fill="url(#photo-tone)" role="img" aria-label="Photo of a home kitchen with washing machine and computer on the worktop"/>
    </svg>
    <div class="headline">Looking for a lodger?</div>
    <div class="tagline">great way to find a suitable lodger</div>
    <div class="brand-name">roomhavenly.net</div>
    <div class="cta">Click Here!</div>
  </section>
</body>
</html>
```